Marlo Tidy Yard Website

We need a website design for this new company. I've attached the Kestrel Works. This company is in the construction industry that provides general labor, maintenance and cleaning for construction sites. We want a clean and simple website that can be easy to navigate.

Target Market(s)

Construction industry

Industry/Entity Type

Construction

Number of Pages Required

2 page

Font styles to use
Sans Serif

```html
<!DOCTYPE html>
<html lang="en">
<head>
<meta charset="utf-8">
<title>Marlo Tidy Yard</title>
<link rel="stylesheet" href="https://fonts.googleapis.com/css2?family=Archivo+Black&family=Montserrat:wght@400;500;600;700&display=swap">
<style>
  :root {
    --navy: #0b0e6b;
    --orange: #f2680f;
    --white: #ffffff;
    --ink: #2b2b2b;
    --soft-bg: #f5f6f8;
    --line: #e3e4e8;
    --purple: #4a4398;
  }
  * { box-sizing: border-box; margin: 0; padding: 0; }
  html, body { width: 1200px; height: 2368px; overflow: hidden; }
  body { font-family: "Montserrat", Arial, sans-serif; color: var(--ink); background: var(--white); position: relative; }
  .display { font-family: "Archivo Black", "Arial Black", sans-serif; }

  /* Hero */
  .hero { position: absolute; left: 0; top: 0; width: 1200px; height: 600px; overflow: hidden; }
  .hero-photo { position: absolute; inset: 0; background: linear-gradient(160deg, #7c7570 0%, #8b7b74 35%, #6f6a66 60%, #5d5b59 100%); }
  .hero-band { position: absolute; left: 0; bottom: 0; }
  .brand-header { position: absolute; left: 122px; top: 24px; display: flex; align-items: center; gap: 10px; }
  .brand-square { width: 22px; height: 22px; background: var(--orange); }
  .brand-header .brand-name { font-family: "Archivo Black", sans-serif; color: var(--white); font-size: 26px; line-height: 1.05; width: 150px; }
  .main-nav { position: absolute; top: 26px; left: 525px; display: flex; align-items: center; gap: 0; }
  .main-nav a { color: var(--white); text-decoration: none; font-size: 13px; letter-spacing: 0.3px; text-transform: uppercase; margin-right: 35px; }
  .main-nav a.active { color: var(--orange); }
  .nav-phone { display: flex; align-items: center; gap: 8px; color: var(--white); font-weight: 700; font-size: 17px; }
  .hero-arrow { position: absolute; top: 328px; width: 30px; height: 34px; border: 1px solid rgba(255,255,255,.5); display: flex; align-items: center; justify-content: center; }
  .hero-arrow.prev { left: 52px; }
  .hero-arrow.next { left: 1118px; }
  .hero-title { position: absolute; top: 388px; left: 0; width: 1200px; text-align: center; color: var(--white); font-size: 37px; line-height: 48px; text-transform: uppercase; text-shadow: 0 2px 4px rgba(0,0,0,.35); }

  /* About */
  .about { position: absolute; top: 600px; left: 0; width: 1200px; height: 372px; }
  .about-brand { position: absolute; left: 120px; top: 680px; top: 80px; display: flex; align-items: center; gap: 14px; }
  .about-brand .brand-square { width: 34px; height: 34px; }
  .about-brand .brand-name { font-family: "Archivo Black", sans-serif; color: var(--navy); font-size: 44px; line-height: 1.05; width: 280px; }
  .about-divider { position: absolute; left: 450px; top: 75px; width: 2px; height: 85px; background: var(--navy); }
  .about-copy { position: absolute; left: 520px; top: 72px; width: 560px; }
  .about-copy h2 { color: var(--navy); font-size: 16.5px; font-weight: 700; line-height: 28px; margin-bottom: 12px; }
  .about-copy p { font-size: 13.2px; line-height: 27px; color: #333; }
  .read-more { display: inline-block; margin-top: 10px; color: var(--orange); font-size: 12.5px; font-weight: 700; text-decoration: underline; text-transform: uppercase; }

  /* Services */
  .services { position: absolute; top: 972px; left: 0; width: 1200px; height: 631px; background: var(--soft-bg); }
  .section-title { text-align: center; color: var(--navy); font-size: 33px; letter-spacing: 1px; }
  .services .section-title { margin-top: 72px; }
  .service-card { position: absolute; top: 151px; width: 300px; height: 390px; background: var(--white); box-shadow: 0 2px 6px rgba(0,0,0,.12); text-align: center; }
  .service-photo { position: relative; height: 190px; overflow: hidden; }
  .service-photo .fill { position: absolute; inset: 0; }
  .service-photo svg { position: absolute; left: 0; bottom: 0; }
  .service-icon { position: absolute; left: 120px; top: 154px; width: 62px; height: 62px; border-radius: 50%; background: var(--navy); display: flex; align-items: center; justify-content: center; }
  .service-card h3 { margin-top: 62px; color: var(--orange); font-size: 19px; letter-spacing: 1px; text-transform: uppercase; }
  .service-card p { margin: 12px auto 0; width: 250px; font-size: 13.6px; line-height: 24px; color: #333; }
  .service-go { position: absolute; left: 134px; bottom: -17px; width: 33px; height: 33px; border-radius: 50%; background: var(--navy); display: flex; align-items: center; justify-content: center; }

  /* Call to action */
  .cta { position: absolute; top: 1603px; left: 0; width: 1200px; height: 344px; text-align: center; color: var(--white); }
  .cta-photo { position: absolute; inset: 0; background: linear-gradient(100deg, #3e3886 0%, #5a54a8 40%, #6c66b6 65%, #4d4699 100%); }
  .cta-content { position: relative; padding-top: 73px; }
  .cta h2 { font-family: "Montserrat", sans-serif; font-weight: 700; font-size: 29.5px; }
  .cta p { font-size: 22.5px; line-height: 36px; margin: 10px auto 0; width: 900px; }
  .cta-button { display: inline-block; margin-top: 22px; background: var(--orange); color: var(--white); font-weight: 700; font-size: 14.5px; padding: 12px 18px; text-transform: uppercase; letter-spacing: .3px; }

  /* Clients */
  .clients { position: absolute; top: 1947px; left: 0; width: 1200px; height: 300px; }
  .clients .section-title { margin-top: 74px; }
  .client-row { position: absolute; top: 147px; left: 121px; display: flex; gap: 15px; }
  .client-tile { width: 181px; height: 94px; border: 1px solid var(--line); display: flex; align-items: center; justify-content: center; gap: 8px; color: #3b3b3b; font-weight: 600; font-size: 17px; }
  .client-tile .dot { width: 12px; height: 12px; border-radius: 50%; background: #3b3b3b; }

  /* Footer */
  .footer-band { position: absolute; left: 0; top: 2250px; }
  .site-footer { position: absolute; top: 2299px; left: 0; width: 1200px; height: 69px; background: var(--navy); color: var(--white); }
  .copyright { position: absolute; left: 121px; top: 27px; font-size: 12.5px; }
  .footer-brand { position: absolute; left: 520px; top: 22px; width: 160px; text-align: center; font-family: "Archivo Black", sans-serif; font-size: 17px; }
  .social-links { position: absolute; left: 944px; top: 18px; display: flex; gap: 10px; }
  .social-links span { width: 30px; height: 30px; border: 1.5px solid var(--white); border-radius: 50%; }
</style>
</head>
<body>

<header class="hero">
  <div class="hero-photo" role="img" aria-label="Photo of a worker in an orange shirt sweeping debris on a construction site in front of a brick building"></div>
  <svg class="hero-band" width="1200" height="50" viewBox="0 0 1200 50" aria-hidden="true">
    <polygon points="0,50 1200,0 1200,50" fill="#f2680f"/>
  </svg>
  <div class="brand-header"><span class="brand-square"></span><span class="brand-name">Marlo Tidy Yard</span></div>
  <nav class="main-nav">
    <a href="#" class="active">Home</a>
    <a href="#">About Us</a>
    <a href="#">Services</a>
    <a href="#">Contact Us</a>
    <span class="nav-phone">
      <svg width="20" height="20" viewBox="0 0 20 20" aria-hidden="true"><circle cx="10" cy="10" r="9" fill="none" stroke="#f2680f" stroke-width="1.6"/><path d="M7 5.5l2 2-1.2 1.3c.7 1.3 1.7 2.3 3 3l1.3-1.2 2 2-1.3 1.4c-2.8-.3-6.2-3.7-6.5-6.5z" fill="#f2680f"/></svg>
      555-014-2290
    </span>
  </nav>
  <span class="hero-arrow prev"><svg width="10" height="16" viewBox="0 0 10 16"><path d="M8 2L2 8l6 6" fill="none" stroke="#fff" stroke-width="2"/></svg></span>
  <span class="hero-arrow next"><svg width="10" height="16" viewBox="0 0 10 16"><path d="M2 2l6 6-6 6" fill="none" stroke="#fff" stroke-width="2"/></svg></span>
  <h1 class="hero-title display">Don’t stress we’ll handle<br>the mess</h1>
</header>

<section class="about">
  <div class="about-brand"><span class="brand-square"></span><span class="brand-name">Marlo Tidy Yard</span></div>
  <div class="about-divider"></div>
  <div class="about-copy">
    <h2>About praesent sit amet diam tincidunt, convallis turpis eu, cursus diam mauris porta, neque et viverra aliquet est libero.</h2>
    <p>Lorem ipsum dolor sit amet, consectetur adipiscing elit, sed do eiusmod tempor incididunt ut labore et dolore magna aliqua. Ut enim ad minim veniam, quis nostrud exercitation ullamco laboris nisi ut aliquip ex ea commodo consequat. Duis aute irure dolor in reprehenderit in voluptate velit esse cillum dolore eu fugiat nulla pariatur.</p>
    <a class="read-more" href="#">Read More</a>
  </div>
</section>

<section class="services">
  <h2 class="section-title display">OUR SERVICES</h2>

  <article class="service-card" style="left:121px">
    <div class="service-photo">
      <div class="fill" role="img" aria-label="Photo of a crew in orange vests and hard hats working on wet concrete" style="background:linear-gradient(170deg,#8d8a86,#6d665f 55%,#a9764f)"></div>
      <svg width="300" height="36" viewBox="0 0 300 36" aria-hidden="true"><path d="M0,0 Q150,40 300,0 L300,36 L0,36Z" fill="#fff"/></svg>
    </div>
    <span class="service-icon"><svg width="30" height="30" viewBox="0 0 30 30"><circle cx="15" cy="10" r="5" fill="none" stroke="#fff" stroke-width="2"/><path d="M8 9h14" stroke="#fff" stroke-width="2"/><path d="M6 26c0-5 4-8 9-8s9 3 9 8z" fill="#fff"/></svg></span>
    <h3 class="display">General Labor</h3>
    <p>Donec bibendum orci id molestie blandit. Vestibulum augue nisl, vehicula a fringilla et, tempor nisi.</p>
    <span class="service-go"><svg width="10" height="12" viewBox="0 0 10 12"><path d="M3 2l4 4-4 4" fill="none" stroke="#fff" stroke-width="2"/></svg></span>
  </article>

  <article class="service-card" style="left:450px">
    <div class="service-photo">
      <div class="fill" role="img" aria-label="Photo of workers in safety vests maintaining a site near a house" style="background:linear-gradient(170deg,#9c948a,#7a7067 55%,#8f8a7d)"></div>
      <svg width="300" height="36" viewBox="0 0 300 36" aria-hidden="true"><path d="M0,0 Q150,40 300,0 L300,36 L0,36Z" fill="#fff"/></svg>
    </div>
    <span class="service-icon"><svg width="30" height="30" viewBox="0 0 30 30"><circle cx="15" cy="15" r="6" fill="none" stroke="#fff" stroke-width="2"/><circle cx="15" cy="15" r="11" fill="none" stroke="#fff" stroke-width="2" stroke-dasharray="4 3"/></svg></span>
    <h3 class="display">Maintenance</h3>
    <p>Donec bibendum orci id molestie blandit. Vestibulum augue nisl, vehicula a fringilla et, tempor nisi.</p>
    <span class="service-go"><svg width="10" height="12" viewBox="0 0 10 12"><path d="M3 2l4 4-4 4" fill="none" stroke="#fff" stroke-width="2"/></svg></span>
  </article>

  <article class="service-card" style="left:779px">
    <div class="service-photo">
      <div class="fill" role="img" aria-label="Photo of a worker pressure washing a concrete surface" style="background:linear-gradient(170deg,#b3ada4,#8a857e 55%,#a5a09a)"></div>
      <svg width="300" height="36" viewBox="0 0 300 36" aria-hidden="true"><path d="M0,0 Q150,40 300,0 L300,36 L0,36Z" fill="#fff"/></svg>
    </div>
    <span class="service-icon"><svg width="30" height="30" viewBox="0 0 30 30"><circle cx="12" cy="7" r="3.5" fill="#fff"/><path d="M8 13h8v7h-2v7h-4v-7H8z" fill="#fff"/><path d="M19 6l4 18" stroke="#fff" stroke-width="2"/><path d="M20 24h6v3h-6z" fill="#fff"/></svg></span>
    <h3 class="display">Cleaning</h3>
    <p>Donec bibendum orci id molestie blandit. Vestibulum augue nisl, vehicula a fringilla et, tempor nisi.</p>
    <span class="service-go"><svg width="10" height="12" viewBox="0 0 10 12"><path d="M3 2l4 4-4 4" fill="none" stroke="#fff" stroke-width="2"/></svg></span>
  </article>
</section>

<section class="cta">
  <div class="cta-photo" role="img" aria-label="Photo of a worker in jeans sweeping dust with a broom, under a purple tint"></div>
  <div class="cta-content">
    <h2>Marlo Tidy Yard Provides Construction Cleanup Services</h2>
    <p>for clients in various industries, from large jobs to small. We know our clients businesses are growing and changing.</p>
    <a class="cta-button" href="#">Contact Us Today</a>
  </div>
</section>

<section class="clients">
  <h2 class="section-title display">OUR CLIENTS</h2>
  <div class="client-row">
    <div class="client-tile"><span class="dot"></span>Norvale</div>
    <div class="client-tile">Brightpine</div>
    <div class="client-tile">Kestrel Works</div>
    <div class="client-tile">Oakridge Civil</div>
    <div class="client-tile"><span class="dot"></span>Halvern</div>
  </div>
</section>

<svg class="footer-band" width="1200" height="50" viewBox="0 0 1200 50" aria-hidden="true">
  <polygon points="0,0 0,50 1200,50 1200,46" fill="#f2680f"/>
</svg>
<footer class="site-footer">
  <p class="copyright">Copyright © 2019 Marlo Tidy Yard. All Rights Reserved.</p>
  <div class="footer-brand">Marlo Tidy Yard</div>
  <div class="social-links" aria-label="Social links">
    <span></span><span></span><span></span><span></span>
  </div>
</footer>

</body>
</html>
```